December online webinar for our coaching and mentoring business.

needing an email flyer and something to use on appropriate social media e.g. Instagram to promote our December half day webinar focusing on positive mindset, relationships and 2021 being a new year with new opportunities. For the feel of what we have done previously:
www.qlvgetaways.com.au
We will be using 2 guest speakers:
Dominic Farrow of 60Quests.com and
Marisa Holt, psychologist and both will need to be prominent on the marketing material we send out on email and use on social media.
The webinar will likely run Thursday December 10th from 12.30pm to 4.30pm AEST and will be hosted and facilitated by me and on behalf of Portwell Business Coaching.
I am thinking colour schemes and branding similar to what you see on the website above.
Pricing needs to be on the flyer - $750 + GST per person*
*enquire for multi booking discounts for 2 people or more

Target Market(s)

people looking for a boost before the year end and a fast start to 2021

Font styles to use
Sans Serif

Requirements
Must have
• see brief above
Nice to have
• see brief above
Should not have
• see brief above

```html
<!DOCTYPE html>
<html lang="en">
<head>
<meta charset="utf-8">
<title>Positive Mindset, Relationships and 2021 – Webinar</title>
<link rel="stylesheet" href="https://fonts.googleapis.com/css2?family=Poppins:wght@400;700&display=swap">
<style>
  :root {
    --brand-red: #e9443b;
    --accent-red: #db3535;
    --ink: #111111;
    --paper: #ffffff;
    --sun-yellow: #f1e73a;
    --mist-grey: #e3e3e1;
  }
  * { margin: 0; padding: 0; box-sizing: border-box; }
  html, body { width: 1200px; height: 628px; overflow: hidden; background: var(--paper); }
  body { font-family: "Poppins", sans-serif; color: var(--ink); }
  .flyer { position: relative; width: 1200px; height: 628px; overflow: hidden; background: var(--paper); }
  .shapes { position: absolute; inset: 0; }
  .headline { position: absolute; left: 66px; top: 66px; }
  .headline__main { font-weight: 700; font-size: 46px; line-height: 56px; letter-spacing: -0.3px; }
  .headline__sub { font-weight: 400; font-size: 28px; line-height: 38px; margin-top: 8px; }
  .event-box {
    position: absolute; left: 66px; top: 315px; width: 398px; height: 126px;
    background: var(--paper); border: 3px solid var(--brand-red); border-radius: 28px;
    padding: 14px 0 0 24px; color: var(--brand-red);
  }
  .event-box__line { font-size: 23px; line-height: 30px; font-weight: 400; white-space: nowrap; }
  .event-box__line strong { font-weight: 700; }
  .event-box__price { font-size: 14px; line-height: 22px; margin-top: 4px; }
  .brand-name {
    position: absolute; left: 66px; top: 536px; color: var(--paper);
    font-weight: 700; font-size: 22px; line-height: 28px;
  }
  .speaker { position: absolute; }
  .speaker__name { color: var(--brand-red); font-size: 31px; line-height: 36px; white-space: nowrap; }
  .speaker__name strong { font-weight: 700; }
  .speaker__role { font-size: 19px; line-height: 26px; }
  .speaker--one { right: 454px; top: 124px; text-align: right; }
  .speaker--two { left: 857px; top: 484px; }
</style>
</head>
<body>
<main class="flyer">
  <svg class="shapes" width="1200" height="628" viewBox="0 0 1200 628" aria-hidden="false">
    <defs>
      <linearGradient id="portrait-one" x1="0" y1="0" x2="1" y2="1">
        <stop offset="0" stop-color="#d9cfa8"/>
        <stop offset="0.5" stop-color="#2d7fb0"/>
        <stop offset="1" stop-color="#1f5f8a"/>
      </linearGradient>
      <linearGradient id="portrait-two" x1="0" y1="0" x2="0" y2="1">
        <stop offset="0" stop-color="var(--sun-yellow)"/>
        <stop offset="0.45" stop-color="#7d6a5c"/>
        <stop offset="1" stop-color="#3e4247"/>
      </linearGradient>
    </defs>
    <polygon class="corner-band" points="0,323 525,628 0,628" fill="var(--brand-red)"/>
    <polygon points="767,127 1102,188 886,453" fill="url(#portrait-one)" role="img" aria-label="Portrait photo of speaker Marisa Holt, smiling, in a blue blouse"/>
    <polygon points="556,347 863,277 811,610" fill="url(#portrait-two)" role="img" aria-label="Photo of speaker Dominic Farrow presenting on stage in a grey T-shirt"/>
    <polygon points="1041,113 1107,85 1100,155" fill="var(--accent-red)"/>
    <polygon points="623,237 662,217 660,260" fill="var(--accent-red)"/>
    <polygon points="521,413 610,443 539,507" fill="var(--accent-red)"/>
    <polygon points="985,366 1028,364 1010,403" fill="var(--accent-red)"/>
  </svg>

  <header class="headline">
    <h1 class="headline__main">Positive Mindset,<br>Relationships</h1>
    <p class="headline__sub">and 2021 with<br>new opportunities</p>
  </header>

  <section class="event-box">
    <p class="event-box__line"><strong>December 10th</strong> Thursday</p>
    <p class="event-box__line">from <strong>12.30pm to 4.30pm</strong> AEST</p>
    <p class="event-box__price">Investment $750 + GST per person*</p>
  </section>

  <p class="brand-name">Portwell Business Coaching</p>

  <div class="speaker speaker--one">
    <p class="speaker__name"><strong>MARISA</strong> Holt</p>
    <p class="speaker__role">Psychologist</p>
  </div>

  <div class="speaker speaker--two">
    <p class="speaker__name"><strong>DOMINIC</strong> Farrow</p>
    <p class="speaker__role">60Quests.com</p>
  </div>
</main>
</body>
</html>
```